Tri-fold Brochure Design for Banking Business

The brochure we have needs to be improved - more business like and more attractive. Logo file and brochure is attached. I would like to be able to edit the text after you get done. Your ideas and changes to text are welcome. See our website www.quillbrookadvisory.com for our theme. We can use indesign to edit the text after you complete. However, please make changes to the text we have in the design that it uploaded. Your comments and changes are welcome.

Target Market(s)

Human Resources and learning & development staff at the global investment banks - Fenwright Carrow, QTRV, etc.

Industry/Entity Type

Investment Banking

Logo Text

Quillbrook Advisory Group

Font styles to use
Serif
Sans Serif

Colors
33a6d7
0493ce
3277b5
fbf289
fdf9cf
fbee3e
0555a3
85acd3

Requirements
Must have
• Must be similar to our website www.quillbrookadvisory.com. Needs to be business-like, clean fonts, sharp design. Our logo - of course.
Nice to have
• City images - seems to be our theme.

```html
<!DOCTYPE html>
<html lang="en">
<head>
<meta charset="utf-8">
<title>Quillbrook Advisory Group – Tri-fold Brochure</title>
<link rel="stylesheet" href="https://fonts.googleapis.com/css2?family=Barlow+Semi+Condensed:wght@300;400;600&display=swap">
<style>
  :root {
    --page-bg: #fef1d0;
    --paper: #ffffff;
    --ink: #1b1b1b;
    --blue: #4a8cc1;
    --blue-deep: #3a76b0;
    --blue-light: #8bb4e0;
    --map-blue: #38a6d8;
    --band-line: #e4eef8;
    --white: #ffffff;
  }
  html, body {
    margin: 0;
    padding: 0;
    width: 960px;
    height: 1200px;
    overflow: hidden;
    background: var(--page-bg);
    font-family: "Barlow Semi Condensed", "Arial Narrow", sans-serif;
  }
  .brochure {
    position: absolute;
    left: 58px;
    top: 178px;
    width: 1054px;
    height: 815px;
    transform: scale(0.8);
    transform-origin: 0 0;
    background: var(--paper);
    box-shadow: 4px 5px 6px rgba(0,0,0,0.28);
    overflow: hidden;
    color: var(--ink);
  }
  .backdrop { position: absolute; left: 0; top: 0; }
  .abs { position: absolute; margin: 0; }

  .section-title {
    font-size: 16px;
    font-weight: 400;
    letter-spacing: 0.62em;
  }
  .about-title { left: 110px; top: 42px; }
  .touch-title { left: 427px; top: 42px; }

  .about-copy {
    left: 33px; top: 76px; width: 280px;
    font-size: 13px; line-height: 16px;
  }
  .about-copy p { margin: 0 0 15px; }

  .photo-london {
    left: -6px; top: 203px; width: 318px; height: 290px;
    border: 5px solid var(--band-line);
    border-radius: 0 20px 20px 0;
    background: linear-gradient(180deg, #a9c6dc 0%, #d2dfe6 38%, #5f8aa6 60%, #35607c 100%);
  }
  .map-area {
    left: 364px; top: 78px; width: 316px; height: 158px;
    border-radius: 40px 60px 30px 50px;
    background: var(--map-blue);
  }
  .photo-skyline {
    left: 525px; top: 187px; width: 529px; height: 285px;
    clip-path: polygon(0 65px, 529px 0, 529px 245px, 272px 285px, 0 255px);
    background: linear-gradient(160deg, #f6e3a8 0%, #efbd66 35%, #c7743a 70%, #8e4a2a 100%);
  }

  .headline-small { left: 379px; top: 292px; font-size: 27px; font-weight: 400; }
  .headline-large {
    left: 379px; top: 329px;
    font-size: 34px; font-weight: 300; line-height: 34px;
    color: var(--white);
  }

  .contacts { left: 379px; top: 469px; color: var(--white); }
  .contact { margin: 0 0 8px; font-size: 15px; line-height: 19px; }
  .contact-region { display: block; font-weight: 600; font-size: 14px; }
  .contact-email { display: block; font-weight: 300; }

  .team-note {
    left: 33px; top: 519px; width: 275px;
    font-size: 12.5px; font-weight: 300; line-height: 16px;
    color: #e8f1fa;
  }
  .quote {
    left: 30px; top: 578px; width: 290px;
    font-size: 23px; font-weight: 600; line-height: 29px;
    color: var(--white);
  }
  .quote-body { display: block; padding-left: 12px; text-indent: -12px; }

  .brand {
    left: 737px; top: 105px;
    display: flex; align-items: center; gap: 12px;
  }
  .brand-mark {
    width: 30px; height: 30px; border-radius: 50%;
    background: var(--blue-deep);
  }
  .brand-name {
    font-size: 23px; font-weight: 600; line-height: 24px;
    color: var(--ink); width: 190px;
  }

  .tagline {
    left: 740px; top: 511px; width: 280px;
    text-align: center;
    font-size: 23px; font-weight: 300; line-height: 29px;
    color: var(--white);
  }
  .website {
    left: 740px; top: 763px; width: 280px;
    text-align: center;
    font-size: 15px; color: #22354a;
  }
</style>
</head>
<body>
<div class="brochure">
  <svg class="backdrop" width="1054" height="815" viewBox="0 0 1054 815" aria-hidden="true">
    <rect x="0" y="327" width="1054" height="488" fill="var(--blue)"/>
    <polygon points="510,262 525,260 525,470 510,470" fill="var(--blue-deep)"/>
    <polygon points="525,445 797,474 1040,434 1040,460 797,484 560,455" fill="var(--blue-deep)"/>
    <polygon points="0,772 645,772 712,737 1054,737 1054,815 0,815" fill="var(--blue-light)"/>
    <polyline points="0,772 645,772 712,737 1054,737" fill="none" stroke="var(--band-line)" stroke-width="5"/>
  </svg>

  <h2 class="abs section-title about-title">ABOUT US</h2>
  <div class="abs about-copy">
    <p>Quillbrook Advisory Group efficiently provides complete sales, marketing and logistical support for all our programs, no matter the location.</p>
    <p>Our globally located trainers have extensive experience, both as industry professionals and as trainers.</p>
  </div>

  <div class="abs photo-london" role="img" aria-label="Photo of a riverside city skyline with a tall glass tower"></div>

  <h2 class="abs section-title touch-title">GET IN TOUCH</h2>
  <div class="abs map-area" role="img" aria-label="World map illustration"></div>

  <div class="abs photo-skyline" role="img" aria-label="Aerial photo of a city skyline and bridge at golden sunset"></div>

  <p class="abs headline-small">Worldwide</p>
  <p class="abs headline-large">Training<br>Service</p>

  <div class="abs contacts">
    <p class="contact"><span class="contact-region">UNITED STATES:</span><span class="contact-email">jared.ardent@quillbrookadvisory.com</span></p>
    <p class="contact"><span class="contact-region">ASIA:</span><span class="contact-email">milo.hastring@quillbrookadvisory.com</span></p>
    <p class="contact"><span class="contact-region">EUROPE:</span><span class="contact-email">marcus.delwyn@quillbrookadvisory.com</span></p>
    <p class="contact"><span class="contact-region">GLOBAL:</span><span class="contact-email">livia.corsetti@quillbrookadvisory.com</span></p>
  </div>

  <p class="abs team-note">Our highly qualified logistical team complement the training services, providing reliable and efficient support.</p>
  <p class="abs quote"><span class="quote-body">“a high level of service using trainers that you are accustomed to using”</span></p>

  <div class="abs brand">
    <span class="brand-mark"></span>
    <span class="brand-name">Quillbrook Advisory Group</span>
  </div>

  <p class="abs tagline">Your Expert Training<br>and Consulting Partner</p>
  <p class="abs website">www.quillbrookadvisory.com</p>
</div>
</body>
</html>
```